Veltrano - Mechanic/Collision Center Business Card

We're looking for a business card design for our mechanic/ collision repair shop.

Can be with colours or monochromatic.

See the attached files.

Many thanks

```html
<!DOCTYPE html>
<html lang="en">
<head>
<meta charset="utf-8">
<title>Veltrano – Business Card</title>
<link href="https://fonts.googleapis.com/css2?family=Open+Sans:wght@400;600;800&display=swap" rel="stylesheet">
<style>
  :root {
    --backdrop: #3b3b3d;
    --card: #2a2a2b;
    --card-back: #262627;
    --ink: #f2f2f2;
    --ink-soft: #d9d9d9;
    --accent: #1f8fd8;
    --emboss: #3a3a3c;
    --deco-grey: #343436;
    --deco-blue: #23394a;
  }
  * { margin: 0; padding: 0; box-sizing: border-box; }
  html, body { width: 1200px; height: 1021px; overflow: hidden; }
  body {
    background: var(--backdrop);
    font-family: "Open Sans", sans-serif;
    display: flex;
    flex-direction: column;
    align-items: center;
    justify-content: center;
    gap: 44px;
  }
  .card {
    position: relative;
    width: 760px;
    height: 434px;
    border-radius: 3px;
    overflow: hidden;
    box-shadow: 0 14px 30px rgba(0,0,0,.35);
  }
  /* Brand side */
  .card--brand {
    background: var(--card-back);
    display: flex;
    align-items: center;
    justify-content: center;
  }
  .brand-emboss {
    display: flex;
    align-items: center;
    gap: 18px;
    color: var(--emboss);
    font-weight: 800;
    font-size: 64px;
    letter-spacing: 2px;
  }
  .brand-emboss .dot {
    width: 40px; height: 40px; border-radius: 50%;
    background: var(--emboss);
  }
  /* Details side */
  .card--details { background: var(--card); }
  .brand {
    position: absolute;
    left: 56px; top: 52px;
    display: flex;
    align-items: center;
    gap: 12px;
    color: var(--ink);
    font-weight: 800;
    font-size: 40px;
    letter-spacing: 1px;
  }
  .brand .dot {
    width: 26px; height: 26px; border-radius: 50%;
    background: var(--accent);
  }
  .contact {
    position: absolute;
    left: 56px; top: 138px;
    list-style: none;
    color: var(--ink-soft);
    font-size: 17px;
    line-height: 25px;
  }
  .contact li { display: flex; align-items: center; gap: 8px; }
  .contact .address { padding-left: 0; }
  .contact svg { width: 16px; height: 16px; flex: none; }
  .contact .social-dot {
    width: 15px; height: 15px; border-radius: 50%;
    background: var(--accent); flex: none;
  }
  .person {
    position: absolute;
    right: 60px; top: 150px;
    text-align: right;
  }
  .person .name {
    color: var(--accent);
    font-size: 25px;
    font-weight: 600;
    letter-spacing: .5px;
  }
  .person .role {
    color: var(--ink);
    font-size: 18px;
    letter-spacing: .5px;
  }
  .decoration {
    position: absolute;
    right: 0; bottom: 0;
    width: 420px; height: 190px;
    background: linear-gradient(90deg, var(--deco-grey) 0%, var(--deco-blue) 70%, var(--deco-grey) 100%);
    opacity: .8;
    border-top-left-radius: 40px;
  }
</style>
</head>
<body>
  <section class="card card--brand">
    <div class="brand-emboss"><span class="dot"></span>VELTRANO</div>
  </section>

  <section class="card card--details">
    <div class="brand"><span class="dot"></span>VELTRANO</div>

    <ul class="contact">
      <li>Veltrano, LDA</li>
      <li>Rua das Oficinas, 42</li>
      <li>1900-318 Lisboa</li>
      <li>
        <svg viewBox="0 0 16 16"><path fill="#1f8fd8" d="M3.5 1.5l2.5 0 1 3.5-1.6 1.2a8 8 0 0 0 4.4 4.4L11 9l3.5 1v2.5c0 .9-.8 1.6-1.7 1.5C7.2 13.4 2.6 8.8 2 3.2 1.9 2.3 2.6 1.5 3.5 1.5z"/></svg>
        +351 210457382
      </li>
      <li>
        <svg viewBox="0 0 16 16"><rect x="4" y="1" width="8" height="14" rx="1.5" fill="none" stroke="#1f8fd8" stroke-width="1.5"/><circle cx="8" cy="12.3" r="0.9" fill="#1f8fd8"/></svg>
        +351 912604718
      </li>
      <li>
        <svg viewBox="0 0 16 16"><rect x="1" y="3" width="14" height="10" fill="none" stroke="#1f8fd8" stroke-width="1.5"/><path d="M1.5 3.5L8 9l6.5-5.5" fill="none" stroke="#1f8fd8" stroke-width="1.5"/></svg>
        veltrano.oficina@mailbox.pt
      </li>
      <li><span class="social-dot"></span>www.veltrano.pt/social</li>
    </ul>

    <div class="person">
      <div class="name">RUI MARQUES</div>
      <div class="role">MANAGER</div>
    </div>

    <div class="decoration" role="img" aria-label="Faint background artwork of the brand emblem"></div>
  </section>
</body>
</html>
```